Webdesign für SEO-Agentur
Zielgruppe
Wir bieten kleinen und mittelständischen Unternehmen Suchmaschinenoptimierung zum fairen Preis mit Erfolgsgarantie an. Unsere Zielgruppe sind Unternehmer die bisher wenig oder gar keine Erfahrungen mit SEO hatten. Wir möchten Unternehmen dabei helfen ihren digitalen Auftritt sowie dessen Sichtbarkeit zu verbessern um neue Kunden zu finden.
Aufgabenstellung
- seriöses und modernes Design bei gleichzeitig ansprechender Gestaltung
- passend zum Namen möchten wir, dass die Website einen leichten wissenschaftlichen/chemischen Touch erhält. Beachten Sie daher unsere Skizze zur Schritt für Schritt Darstellung. Weitere kleine Hinweise in Richtung Chemie oder Wissenschaft können und sollen eingebaut werden.
- vorerst nur Landing-Page, daher keine Navigation nötig. Wir erwarten eine vollständige Desktop sowie Mobilversion in Ihrem Design.
- Einhaltung der vorgegebenen Inhalte
- keine langweiligen Standard-Designs, auch besondere Seiten können seriös sein
- Header ist für Portrait der Mitarbeiter reserviert und benötigt daher eine gewisse freie Fläche

```html
<!DOCTYPE html>
<html lang="de">
<head>
<meta charset="utf-8">
<title>Neon Faktor – SEO Agentur</title>
<link href="https://fonts.googleapis.com/css2?family=Lato:wght@300;400;700&display=swap" rel="stylesheet">
<style>
:root{
  --navy:#0d3358;
  --red:#e8174a;
  --bg:#f6f6f7;
  --edge:#ffffff;
  --text:#6b6b6b;
  --muted:#a3a3a3;
  --card:#ffffff;
  --line:#e4e4e6;
}
*{box-sizing:border-box;margin:0;padding:0}
html,body{width:1200px;height:4167px;overflow:hidden}
body{font-family:'Lato',sans-serif;color:var(--text);background:var(--edge);position:relative}
.page{position:absolute;left:40px;top:0;width:1160px;height:4167px;background:var(--bg);overflow:hidden}
.abs{position:absolute}
p{font-size:13.5px;line-height:21.5px;font-weight:300}
h2{font-weight:400;color:var(--navy);font-size:30px;line-height:44px}
.center{text-align:center}
.shape-navy{left:914px;top:97px;width:300px;height:614px}
.shape-red{left:930px;top:1366px;width:300px;height:600px}
.intro-left{left:97px;top:0;width:300px;font-size:12.5px;line-height:19.5px}
.intro-right{left:680px;top:0;width:343px;text-align:right;font-size:12.5px;line-height:19.5px}
.lab-art{left:480px;top:0;width:220px;height:80px;opacity:.35}
.why-title{left:97px;top:262px;font-size:29px;font-weight:700;color:var(--navy)}
.why-sub{left:97px;top:305px;font-size:19px;font-weight:300;color:var(--muted)}
.why-text{left:97px;top:355px;width:690px}
.grid{left:97px;width:926px;display:grid;grid-template-columns:repeat(3,292px);gap:25px}
.card{background:var(--card);box-shadow:0 1px 3px rgba(0,0,0,.06)}
.card .img{height:194px}
.card .body{padding:30px 25px 25px}
.card h3{color:var(--red);font-size:14.5px;font-weight:700;line-height:19px;margin-bottom:16px}
.card p{font-size:12.5px;line-height:20px}
.row1{top:569px}.row1 .card{height:426px}
.row2{top:1022px}.row2 .card{height:433px}
.photo-left{left:0;top:1600px;width:275px;height:648px}
.cta-title{left:0;width:1160px;top:1630px;font-weight:700;font-size:30px;line-height:37px}
.cta-text{left:255px;width:650px;top:1735px;text-align:center}
.btn{position:absolute;background:var(--red);color:#fff;font-size:14px;font-weight:700;text-align:center;border-radius:22px}
.steps-title{left:0;width:1160px;top:2110px;font-weight:700;font-size:30px;line-height:45px}
.arrow{width:38px;height:38px}
.step-h{left:414px;top:2240px;font-size:19px;font-weight:400;color:#333}
.step-text{left:414px;top:2275px;width:450px}
.hex{left:258px;top:2288px;width:124px;height:140px}
.el-title{left:0;width:1160px;top:2553px;font-weight:700;font-size:30px}
.grid3{top:2647px}.grid3 .card{height:264px}
.grid3 .card .body{padding-top:28px}
.photo-right{left:963px;top:2943px;width:237px;height:534px}
.adv-title{left:0;width:1160px;top:3010px;font-weight:700;font-size:30px}
.adv{position:absolute;display:flex;gap:24px;align-items:flex-start}
.adv b{display:block;color:#333;font-size:14px;font-weight:700;line-height:20px}
.adv span{font-size:14px;font-weight:300;line-height:22px}
.form-title{left:0;width:1160px;top:3372px;font-weight:700;font-size:30px;line-height:37px}
.field{position:absolute;width:368px;height:42px;border-radius:21px;background:#fff;border:1px solid var(--line);padding:0 17px;font-size:12px;font-style:italic;line-height:40px;color:#b8b8b8}
.map{left:505px;top:3825px;width:695px;height:342px}
.contact-title{left:97px;top:3875px;font-size:30px;font-weight:700;color:var(--navy)}
.contact{left:97px;top:3937px;font-size:14px;line-height:22px;font-weight:300;display:flex;gap:50px}
.contact .pair{display:grid;grid-template-columns:70px auto}
.footer{left:97px;top:4134px;font-size:13.5px;font-weight:300;display:flex;gap:36px}
</style>
</head>
<body>
<div class="page">

  <svg class="abs shape-navy" viewBox="0 0 300 614" aria-hidden="true"><path d="M300 0 L300 614 L40 260 Q0 205 40 150 Z" fill="var(--navy)"/></svg>
  <svg class="abs shape-red" viewBox="0 0 300 600" aria-hidden="true"><path d="M300 0 L300 600 L40 260 Q0 205 40 150 Z" fill="var(--red)"/></svg>

  <p class="abs intro-left">wichtiger ist es, mit seiner Webseite genau hier zu ranken. Das aber wollen viele, deshalb führt für erfolgreiche Webseiten kein Weg an der Suchmaschinenoptimierung vorbei. Wir als SEO Agentur unterstützen Sie dabei, aus den zahlreichen Elementen, die für die Suchmaschinenoptimierung notwendig sind, eine funktionierende Verbindung zu schaffen.</p>
  <div class="abs lab-art" role="img" aria-label="Feine Linienillustration von Laborgefäßen" style="background:linear-gradient(90deg,#e9e9eb,#dedee1)"></div>
  <p class="abs intro-right">zahlende Kunden werden. Dadurch steigt nicht nur Ihre Konversionsrate, sondern natürlich auch der Umsatz Ihres Unternehmens. Suchmaschinenoptimierung macht sich also bezahlt!</p>

  <h1 class="abs why-title">Warum wir?</h1>
  <div class="abs why-sub">SEO Agentur mit Herz, Verstand und ganz viel Erfahrung</div>
  <p class="abs why-text">Seit über zehn Jahren forschen wir schwerpunktmäßig an der perfekten Zusammensetzung effektiver Suchmaschinenoptimierung. Als reine SEO Agentur haben wir uns ganz bewusst dafür entschieden, nicht die gesamte Palette des Online Marketings anzubieten, sondern das, wofür unser Herz schlägt und das, was den größten und vor allem nachhaltigsten Erfolg verspricht. Seitdem ist SEO mehr als unser Forschungsgebiet. SEO ist unsere Leidenschaft. Und genau die Liebe zu dem, was wir tun, macht uns so gut, dass wir ausschließlich auf Erfolgsbasis arbeiten.</p>

  <div class="abs grid row1">
    <div class="card"><div class="img" role="img" aria-label="Foto: Berater im Anzug mit Unterlagen im Büro" style="background:linear-gradient(135deg,#d8dadd,#6e6a66)"></div><div class="body"><h3>SEO für Anwälte und Steuerberater</h3><p>Große Rechtanwalts- und Steuerberaterkanzleien dominieren den Markt. Mit SEO können sich auch kleine und regionale Anwälte, Notare, Steuer- und Unternehmensberater durchsetzen. Wir helfen Ihnen, sich online als Experte zu profilieren.</p></div></div>
    <div class="card"><div class="img" role="img" aria-label="Foto: Arzt im Gespräch mit einer Patientin" style="background:linear-gradient(135deg,#e3e6e8,#a79580)"></div><div class="body"><h3>SEO für Ärzte und Apotheker</h3><p>Ärzte und Apotheker können mit einer suchmaschinen-optimierten Webseite nicht nur neue Patienten und Kunden gewinnen, sondern diesen auch langfristig binden und ihnen zeitgemäße Serviceleistungen anbieten.</p></div></div>
    <div class="card"><div class="img" role="img" aria-label="Foto: Übergabe eines Pakets" style="background:linear-gradient(135deg,#d9c9a8,#8c7a52)"></div><div class="body"><h3>SEO für (Online-)Händler</h3><p>Der Online-Handel boomt, entsprechend groß ist auch die Konkurrenz. Ein Online-Shop ist noch lange kein Selbstläufer und bedarf besonderen Know-hows bei der Suchmaschinen-optimierung. Wir steigern Ihre Verkaufszahlen nachhaltig!</p></div></div>
  </div>

  <div class="abs grid row2">
    <div class="card"><div class="img" role="img" aria-label="Foto: Handwerker mit Werkzeuggürtel in der Werkstatt" style="background:linear-gradient(135deg,#b6a389,#5d4a37)"></div><div class="body"><h3>SEO für Handwerker und Dienstleister</h3><p>Wer einen Handwerker oder Dienstleister sucht, der schaut nicht mehr ins Branchenbuch, sondern sucht online. Ohne sichtbare Webseite sind Sie für den Kunden quasi nicht existent. Mit Local SEO lässt sich das bereits mit einfachen Mitteln und für kleines Geld ändern!</p></div></div>
    <div class="card"><div class="img" role="img" aria-label="Foto: Hand skizziert Webseiten-Wireframes an einer Glaswand" style="background:linear-gradient(135deg,#3a3f46,#c9ced3)"></div><div class="body"><h3>SEO für Online-Portale</h3><p>Online-Portale sind von den Suchmaschinen so abhängig wie kaum ein anderes Internetangebot. Nur wer bei Suchfix ganz oben steht, erhält ausreichend Traffic um zu überleben. Wir sichern die Zukunft Ihres Portals und bringen Sie in die schwarzen Zahlen.</p></div></div>
    <div class="card"><div class="img" role="img" aria-label="Foto: Team arbeitet gemeinsam am Computer" style="background:linear-gradient(135deg,#e6e4df,#4a5866)"></div><div class="body"><h3>SEO für Sie</h3><p>Es gibt keine Branche, die heutzutage ohne Suchmaschinenoptimierung auskommt. Mit zielgerichteten Maßnahmen setzen wir auch Ihr Business auf ein neues Level, ganz egal wie groß Ihr Unternehmen ist. Sprechen Sie uns noch heute an!</p></div></div>
  </div>

  <div class="abs photo-left" role="img" aria-label="Foto in Sechseckform: Hand zeichnet Wireframes" style="clip-path:polygon(0 0,40% 20%,100% 55%,0 100%);background:linear-gradient(160deg,#dfe6ea,#8a9aa6)"></div>

  <svg class="abs" style="left:553px;top:1553px" width="54" height="54" viewBox="0 0 54 54" aria-hidden="true" fill="none" stroke="var(--red)" stroke-width="1.6">
    <polygon points="27,15 37,21 37,33 27,39 17,33 17,21"/><polygon points="27,21 32,24 32,30 27,33 22,30 22,24"/>
    <line x1="27" y1="15" x2="27" y2="4"/><line x1="27" y1="39" x2="27" y2="50"/><line x1="17" y1="21" x2="8" y2="15"/><line x1="37" y1="21" x2="46" y2="15"/><line x1="17" y1="33" x2="8" y2="39"/><line x1="37" y1="33" x2="46" y2="39"/>
  </svg>
  <h2 class="abs cta-title center">Lassen Sie sich beraten.<br>Kostenlos und unverbindlich.</h2>
  <p class="abs cta-text">Seit über zehn Jahren forschen wir schwerpunktmäßig an der perfekten Zusammensetzung effektiver Suchmaschinenoptimierung. Als reine SEO Agentur haben wir uns ganz bewusst dafür entschieden, nicht die gesamte Palette des Online Marketings anzubieten, sondern das, wofür unser Herz schlägt und das, was den größten und vor allem nachhaltigsten Erfolg verspricht. Seitdem ist SEO mehr als unser Forschungsgebiet. SEO ist unsere Leidenschaft. Und genau die Liebe zu dem, was wir tun, macht uns so gut, dass wir ausschließlich auf Erfolgsbasis arbeiten.</p>
  <div class="btn" style="left:388px;top:1905px;width:342px;height:42px;line-height:42px">Jetzt unverbindliche Beratung vereinbaren</div>

  <h2 class="abs steps-title center">Wir stellen die richtige Verbindung her<br>Schritt für Schritt zur erfolgreichen Webseite</h2>
  <svg class="abs arrow" style="left:177px;top:2337px" viewBox="0 0 38 38" aria-hidden="true" fill="none" stroke="var(--navy)" stroke-width="1.8"><circle cx="19" cy="19" r="17"/><path d="M27 19H11M17 13l-6 6 6 6"/></svg>
  <svg class="abs arrow" style="left:903px;top:2337px" viewBox="0 0 38 38" aria-hidden="true" fill="none" stroke="var(--navy)" stroke-width="1.8"><circle cx="19" cy="19" r="17"/><path d="M11 19h16M21 13l6 6-6 6"/></svg>
  <svg class="abs hex" viewBox="0 0 124 140" aria-hidden="true">
    <polygon points="62,4 118,36 118,104 62,136 6,104 6,36" fill="#fff" stroke="#dedede" stroke-width="9"/>
    <text x="22" y="52" font-family="Lato,sans-serif" font-size="12" fill="#777">1</text>
    <text x="62" y="86" text-anchor="middle" font-family="Lato,sans-serif" font-size="40" fill="var(--navy)">AL</text>
  </svg>
  <div class="abs step-h">1. Analyse</div>
  <p class="abs step-text">Bevor wir mit der eigentlichen Optimierung beginnen, nehmen wir uns zunächst die Zeit, um uns ein ausgiebiges Bild vom Ist-Zustand zu verschaffen. Dabei prüfen wir unter anderem mithilfe professioneller SEO-Tools, wie gut Ranking und Sichtbarkeit der vorhandenen Webseite sind, um anschließend gezielte Maßnahmen planen und ergreifen zu können. Wir besprechen gemeinsam mit Ihnen die Analyseergebnisse, erfragen Ihre Vorstellungen sowie Ihre Ziele und beraten Sie kostenlos und unverbindlich zu allen Fragen der Suchmaschinenoptimierung.</p>

  <h2 class="abs el-title center">Jedes Element trägt zu Ihrem Erfolg bei</h2>
  <div class="abs grid grid3">
    <div class="card"><div class="body"><h3>Mobile SEO</h3><p>Je nach Branche erfolgt der Großteil der Seitenaufrufe längst über Smartphones und Tablets. Suchfix hat deshalb die Mobile-First-Strategie ausgerufen. Nur wer eine für mobile Endgeräte optimierte Webseite hat, kann Spitzenpositionen in den Suchergebnissen belegen. Wir machen Ihre Webseite fit fürs mobile Zeitalter!</p></div></div>
    <div class="card"><div class="body"><h3>Local SEO</h3><p>50 Prozent der Suchanfragen, die über eine Smartphone getätigt werden, sind lokal. Mit Local SEO beherrschen Sie auch den lokalen Suchindex und können sich über Kunden aus der Umgebung und mit einer deutlich höheren Kaufabsicht freuen – selbst ohne eigene Webseite. Wir zeigen Ihnen, wie das geht!</p></div></div>
    <div class="card"><div class="body"><h3>Image SEO</h3><p>Multimedialer Content spricht die Besucher nicht nur besser an, er gefällt auch den Suchmaschinen. Insbesondere Bilder lassen sich gezielt optimieren, um auch über die Suchfix Bildersuche Traffic zu generieren. Dabei kommt es vor allem darauf an, der Suchmaschine dabei zu helfen, das Motiv zu interpretieren. Wir erschließen gern neue Trafficquellen für Sie!</p></div></div>
  </div>

  <div class="abs photo-right" role="img" aria-label="Foto in Sechseckform: lächelnder Mitarbeiter mit Kaffeetasse" style="clip-path:polygon(100% 0,100% 100%,30% 75%,0 30%);background:linear-gradient(160deg,#c6d0d8,#9c7b5e)"></div>

  <h2 class="abs adv-title center">Ihre Vorteile auf einen Blick:</h2>
  <div class="adv" style="left:97px;top:3104px"><svg width="30" height="30" viewBox="0 0 30 30" fill="none" stroke="var(--red)" stroke-width="1.5" aria-hidden="true"><circle cx="15" cy="15" r="13"/><path d="M9 15l4 4 9-9"/></svg><div><b>mehr Traffic, mehr Kunden, mehr Umsatz</b><span>durch höhere Sichtbarkeit und größere Reichweite</span></div></div>
  <div class="adv" style="left:97px;top:3170px"><svg width="30" height="30" viewBox="0 0 30 30" fill="none" stroke="var(--red)" stroke-width="1.5" aria-hidden="true"><circle cx="15" cy="15" r="13"/><path d="M9 15l4 4 9-9"/></svg><div><b>Fokus auf erfolgreiches SEO</b><span>statt alles anzubieten, aber nichts richtig</span></div></div>
  <div class="adv" style="left:97px;top:3236px"><svg width="30" height="30" viewBox="0 0 30 30" fill="none" stroke="var(--red)" stroke-width="1.5" aria-hidden="true"><circle cx="15" cy="15" r="13"/><path d="M9 15l4 4 9-9"/></svg><div><b>über 10 Jahre SEO-Erfahrung</b><span>mit eigenen Webseiten und Projekten von Kunden</span></div></div>
  <div class="adv" style="left:572px;top:3104px"><svg width="30" height="30" viewBox="0 0 30 30" fill="none" stroke="var(--red)" stroke-width="1.5" aria-hidden="true"><circle cx="15" cy="15" r="13"/><path d="M9 15l4 4 9-9"/></svg><div><b>100 % erfolgsbasiert</b><span>erst bezahlen, wenn Sie auf Seite 1 sind</span></div></div>
  <div class="adv" style="left:572px;top:3170px"><svg width="30" height="30" viewBox="0 0 30 30" fill="none" stroke="var(--red)" stroke-width="1.5" aria-hidden="true"><circle cx="15" cy="15" r="13"/><path d="M9 15l4 4 9-9"/></svg><div><b>kostenlose Beratung</b><span>und unverbindliche Angebotserstellung</span></div></div>

  <h2 class="abs form-title center">Fordern Sie jetzt eine kostenlose und<br>unverbindliche Beratung an</h2>
  <div class="field" style="left:177px;top:3509px">Vorname</div>
  <div class="field" style="left:573px;top:3509px">Name</div>
  <div class="field" style="left:177px;top:3576px">Unternehmen</div>
  <div class="field" style="left:573px;top:3576px">Branche</div>
  <div class="field" style="left:177px;top:3642px">Telefonnummer</div>
  <div class="field" style="left:573px;top:3642px">E-Mail-Adresse</div>
  <div class="btn" style="left:473px;top:3737px;width:174px;height:41px;line-height:41px">Anfrage senden</div>

  <div class="abs map" role="img" aria-label="Stadtplan mit Lage des Büros" style="clip-path:polygon(22% 0,100% 0,100% 100%,0 100%);background:linear-gradient(135deg,#eceef0,#d9dde1)"></div>
  <h2 class="abs contact-title">So erreichen Sie uns</h2>
  <div class="abs contact">
    <div>Neon Faktor GmbH<br>Laborweg 7<br>60311 Beispielstadt</div>
    <div class="pair"><span>Telefon</span><span>069 555 010 220</span><span>E-Mail</span><span>info@neonfaktor.de</span><span>Mo-Fr</span><span>9:00 Uhr - 18:00 Uhr</span></div>
  </div>
  <div class="abs footer"><span>© 2018 Neon Faktor</span><span>Impressum</span></div>
</div>
</body>
</html>
```